Women's Online Clothing Boutique Needs Business Cards

I already have a logo that I would like to use. Some of the things that interest me is black business cards, foil embossed logo, glossy embossed logo, leopard print, no yellow font, rounded edges. I even like just a large logo on the front side with all of my information on the back side.

Contact Information for Business Card

https://silverheron.shopvenlo.com/
https://www.pagelink.net/thesilverheronboutique/
https://www.picfeed.net/thesilverheronboutique/
silverheronboutique@mailora.net

Requirements
Must have
• My Logo
Nice to have
• Leopard Print
Should not have
• No Yellow Font

```html
<!DOCTYPE html>
<html lang="en">
<head>
<meta charset="utf-8">
<title>The Silver Heron Boutique – Business Card</title>
<link rel="stylesheet" href="https://fonts.googleapis.com/css2?family=Roboto+Condensed:wght@400;500&display=swap">
<style>
  :root {
    --card-black: #231f20;
    --gold-light: #f3d27a;
    --gold-mid: #d9a53a;
    --gold-deep: #a8741c;
    --ink: #1c1a17;
    --text-light: #f4f4f4;
    --page: #ffffff;
  }
  * { margin: 0; padding: 0; box-sizing: border-box; }
  html, body {
    width: 1200px;
    height: 686px;
    overflow: hidden;
    background: var(--page);
  }
  .card {
    position: relative;
    width: 1200px;
    height: 686px;
    border-radius: 46px;
    overflow: hidden;
    display: flex;
    background: var(--card-black);
    font-family: "Roboto Condensed", "Arial Narrow", sans-serif;
  }
  .brand-side {
    position: relative;
    width: 600px;
    height: 100%;
    background:
      radial-gradient(ellipse at 30% 25%, rgba(255,240,180,0.55), transparent 55%),
      radial-gradient(ellipse at 75% 80%, rgba(150,95,20,0.45), transparent 60%),
      linear-gradient(135deg, var(--gold-light) 0%, var(--gold-mid) 45%, var(--gold-deep) 100%);
  }
  .brand-name {
    position: absolute;
    left: 0;
    width: 100%;
    top: 300px;
    text-align: center;
    color: var(--ink);
    font-weight: 400;
    line-height: 1.05;
  }
  .brand-name .line-main { display: block; font-size: 56px; }
  .brand-name .line-sub { display: block; font-size: 44px; }
  .contact-side {
    position: relative;
    flex: 1;
    height: 100%;
  }
  .contact-item {
    position: absolute;
    left: 0;
    width: 100%;
    text-align: center;
    color: var(--text-light);
    font-size: 25px;
    font-weight: 400;
  }
  .contact-item .icon {
    display: block;
    width: 44px;
    height: 44px;
    margin: 0 auto 12px;
  }
  .item-page { top: 86px; }
  .item-feed { top: 228px; }
  .item-mail { top: 366px; }
  .item-web { top: 506px; }
</style>
</head>
<body>
  <div class="card">
    <section class="brand-side" role="img" aria-label="Gold foil texture background">
      <div class="brand-name">
        <span class="line-main">The Silver Heron</span>
        <span class="line-sub">Boutique</span>
      </div>
    </section>

    <section class="contact-side">
      <svg width="0" height="0" style="position:absolute">
        <defs>
          <linearGradient id="goldFill" x1="0" y1="0" x2="1" y2="1">
            <stop offset="0" stop-color="#f3d27a"/>
            <stop offset="0.5" stop-color="#d9a53a"/>
            <stop offset="1" stop-color="#a8741c"/>
          </linearGradient>
        </defs>
      </svg>

      <div class="contact-item item-page">
        <svg class="icon" viewBox="0 0 44 44" aria-hidden="true">
          <rect x="2" y="2" width="40" height="40" rx="4" fill="url(#goldFill)"/>
        </svg>
        <span>thesilverheronboutique/</span>
      </div>

      <div class="contact-item item-feed">
        <svg class="icon" viewBox="0 0 44 44" aria-hidden="true">
          <rect x="3" y="3" width="38" height="38" rx="9" fill="none" stroke="url(#goldFill)" stroke-width="4"/>
        </svg>
        <span>thesilverheronboutique/</span>
      </div>

      <div class="contact-item item-mail">
        <svg class="icon" viewBox="0 0 44 44" aria-hidden="true">
          <rect x="3" y="8" width="38" height="28" rx="3" fill="url(#goldFill)"/>
          <path d="M6 12 L22 25 L38 12" fill="none" stroke="#231f20" stroke-width="3"/>
        </svg>
        <span>silverheronboutique@mailora.net</span>
      </div>

      <div class="contact-item item-web">
        <svg class="icon" viewBox="0 0 44 44" aria-hidden="true">
          <g fill="none" stroke="url(#goldFill)" stroke-width="3">
            <circle cx="22" cy="22" r="18"/>
            <ellipse cx="22" cy="22" rx="8" ry="18"/>
            <line x1="22" y1="4" x2="22" y2="40"/>
            <line x1="4" y1="22" x2="40" y2="22"/>
            <path d="M7 13 H37 M7 31 H37"/>
          </g>
        </svg>
        <span>https://silverheron.shopvenlo.com/</span>
      </div>
    </section>
  </div>
</body>
</html>
```